"The Summit Hour Audio Series" needs 3 banner ad designs

I am seeking the design and creation of 3 differently-designed ”banner ads.” I want them to look as though there is a relation between designs but I don't want them to look the same.
While compatibility is desired, that desire should not be interpreted as sameness.

I need a series of banner ads to be a supplement and a complement to
"The Summit Hour"'s main banner ad page and accompanying site.
http://www.quorvale.org/

I am looking for high quality, creative capturing of banner ads that focus on three topic areas, namely, my:

1. Leadership Coaching Program –
“Stride Builder Mentoring Track™”

2. Training program – “The Craft of a Steady Captain”

and

3. Speaker Interest & Availability banner ad.

It is desired that each banner, and the banners collectively, complement and fit in with the look and feel of the existing, principal banner and the show’s vision and mission. (in the attachment, I have included a copy of this banner for your information).

The final design should commit experience, competence, depth and reliability.

To provide a bit of context for this request, I have included the show's vision and mission statement as well as a brief description of my perspective on each banner ad.

I will of course, provide the winner all of the information, documents, graphic depictions, etc that I have available (during the handover stage) that will enable them to create quality products.

In addition, each banner ad should be delivered as JPEG files in dimensions 728 pixel wide and 90 pixels high each. The following fonts: Trajan Pro Regular or Thomas Condensed Regular are the desired fonts.

The task summary: Design 3 banner ads as described below:

1. Leadership Coaching Program – Stride Builder Mentoring Track™
My coaching program has a formal structure that has an existing graphic capturing of leadership coaching that that would/should be incorporated in the ad.

2. Training program – The Craft of a Steady Captain
The skills training program description I have included as noted below; it is a program that can also be licensed for use by customers who would wish to use it in their organization. In addition to the creative thinking of graphics artists, it would probably be useful to view the home page graphic at www.tovrik4.com. This image might be useful in enhancing the banner ad graphic.

3. Speaking Interest – Availability
Have been and desire using this banner to communicate my interest in generating value and availability as a speaker.

-Vision-
“The Summit Hour”
Making an Impact through Effective Leadership
*is a powerfully engaging platform for great conversations about leadership and leadership learning.

-Mission-
Build a community of listeners who are informed and enthusiastically engaged with the host and the show’s goal of improving the quality of leadership wherever listeners are living and leading.

File: "1785 Postcard V2" - *this information is for use in designing the
Leadership Coaching Banner Ad* = *Stride Builder Mentoring Track*

File: "Cover Shot of Skills Book" - *this information is
for use in designing the Book Ad – The Craft of a Steady Captain:
Growing a Guide Whom Peers Gladly Trust*

File: (word doc) The Craft of a Steady Captain Training Workshop – Skills &
Concepts Summary *this information is for the design of the banner ad for
the Skills Training Course. It includes quotes that could be excerpted to
include in the banner ad*

File name: "Cover - Craft of a Steady Captain"
-> Picture of book for Craft of a Steady Captain Training Program – *this is additional information for the use in designing the Training program banner ad

You can find the other attachments useful. Please have a look.
I welcome all your creative and original designs. Remember, these are 3 different-looking banner ads - though related in some way.

Project Deadline Extended Reason: The current designs have not included enough variety and creativity. While I am desirous of compatibility of the ad renditions with the central image, I am not interpreting compatibility with sameness of looking to see the same image in each banner ad. I rather think the image differentiation promotes both interest and distinction between the products of book, leadership coaching, speaking, etc. Same image embedded in each banner ad doesn't provide the variety that I think both distinguishes and draws interest. In this regard, most of the current examples include the same pictorial images across designs and the use of just words vs. images from among those provided, As an example a picture of my book on the book banner ad seems more impactful than merely using the words book on the ad for the book; and the picture of a speaker vs. Speaker Availability.I hope this feedback is helpful . Regards,Leopold Added Saturday, June 3, 2017

Target Market(s)

Online Radio Listeners Can Visit WavelineHub.com for examples - Will be broadcast on the Commerce Channel

Industry/Entity Type

Business Consultant

Colors

Designer to choose colors to be used in the design.

Requirements
Should not have
• Anything that doesn't speak to the characteristics noted at the end of the summary provided in the description above

```html
<!DOCTYPE html>
<html lang="en">
<head>
<meta charset="utf-8">
<title>Stride Builder Mentoring Track – Banner</title>
<link rel="stylesheet" href="https://fonts.googleapis.com/css2?family=Open+Sans:wght@600;700&display=swap">
<style>
  :root {
    --stage: #353535;
    --ink: #55565a;
    --sage: #8faaa3;
    --paper: #ffffff;
    --paper-shade: #e9e9e9;
    --glint: #e4e4e4;
    --photo-light: #eef0ee;
    --photo-mid: #c9d6e4;
  }
  html, body {
    margin: 0;
    width: 1200px;
    height: 1200px;
    overflow: hidden;
    background: var(--stage);
  }
  .banner {
    position: absolute;
    left: 73px;
    top: 422px;
    width: 1054px;
    height: 357px;
    display: block;
  }
  .banner text {
    font-family: "Open Sans", "Myriad Pro", sans-serif;
    fill: var(--ink);
  }
  .title-line-1 { font-size: 46px; font-weight: 700; letter-spacing: -0.5px; }
  .title-line-2 { font-size: 70px; font-weight: 700; letter-spacing: -1px; }
  .author-name { font-size: 22px; font-weight: 700; }
  .badge-text { font-size: 26px; font-weight: 600; }
  .badge-text .accent { fill: var(--sage); }
</style>
</head>
<body>
<svg class="banner" viewBox="0 0 1230 416" xmlns="http://www.w3.org/2000/svg">
  <defs>
    <linearGradient id="paperFade" x1="0" y1="0" x2="0" y2="1">
      <stop offset="0" stop-color="var(--paper-shade)"/>
      <stop offset="0.35" stop-color="var(--paper)"/>
      <stop offset="0.75" stop-color="var(--paper)"/>
      <stop offset="1" stop-color="var(--paper-shade)"/>
    </linearGradient>
    <linearGradient id="photoTone" x1="0" y1="0" x2="1" y2="0">
      <stop offset="0" stop-color="var(--photo-light)"/>
      <stop offset="0.55" stop-color="var(--photo-mid)"/>
      <stop offset="1" stop-color="var(--photo-light)"/>
    </linearGradient>
  </defs>

  <!-- base panel -->
  <rect class="panel" width="1230" height="416" fill="url(#paperFade)"/>

  <!-- sage field -->
  <polygon class="sage-field" points="0,416 0,404 440,300 785,206 893,416" fill="var(--sage)"/>

  <!-- dark sweep band -->
  <polygon class="sweep-band" points="0,318 400,262 400,290 0,364" fill="var(--ink)"/>
  <line class="sweep-line" x1="560" y1="250" x2="782" y2="203" stroke="var(--ink)" stroke-width="4"/>

  <!-- coach portrait area -->
  <g class="coach-photo" role="img" aria-label="Portrait of a smiling coach in a light blue shirt with arms crossed, standing before white bookshelves">
    <polygon points="903,0 1230,0 1230,416 903,416 797,198" fill="url(#photoTone)"/>
  </g>
  <polyline class="chevron-frame" points="900,0 793,198 900,416" fill="none" stroke="var(--ink)" stroke-width="8"/>

  <!-- headline -->
  <text class="title-line-1" x="77" y="75">Stride Builder</text>
  <text class="title-line-2" x="75" y="148">Mentoring Track™</text>
  <text class="author-name" x="80" y="222">LEOPOLD E. HARTWELL</text>

  <!-- badges -->
  <g class="badge badge-learn">
    <circle cx="480" cy="281" r="91" fill="var(--paper)" stroke="var(--ink)" stroke-width="10"/>
    <ellipse cx="477" cy="208" rx="35" ry="14" fill="var(--glint)"/>
    <text class="badge-text" text-anchor="middle">
      <tspan x="479" y="254">LEARN</tspan>
      <tspan class="accent" x="479" y="288">FROM AN</tspan>
      <tspan x="479" y="322">EXPERT</tspan>
    </text>
  </g>
  <g class="badge badge-become">
    <circle cx="670" cy="293" r="87" fill="var(--paper)" stroke="var(--ink)" stroke-width="10"/>
    <ellipse cx="667" cy="226" rx="35" ry="14" fill="var(--glint)"/>
    <text class="badge-text" text-anchor="middle">
      <tspan x="669" y="280">BECOME</tspan>
      <tspan x="671" y="314">AN EXPERT</tspan>
    </text>
  </g>
</svg>
</body>
</html>
```